A new presentation to our clients

we are a Real Estate agency, our website is www.dorelumia.com and it’s time to have a new, fashion and remarcable Business Card. we want to differentiate ourselves from other companies so we want a business card that differentiates us. we want the business card to impact our customers. in the competitive market that we have today, we have to be different and it is this difference that we seek

Target Market(s)

Real Estate Clients

Contact Information for Business Card

We search a totaly diferent card from the usual

Font styles to use
Sans Serif

Colors
e34197

Requirements
Must have
• Logo, adress, phone contact, e-mail, photo, and our website
Nice to have
• We would like to see a modern business card
Should not have
• Houses or building draws

```html
<!DOCTYPE html>
<html lang="en">
<head>
<meta charset="utf-8">
<title>Dore Lumia Business Card</title>
<link href="https://fonts.googleapis.com/css2?family=Arimo:wght@400;700&display=swap" rel="stylesheet">
<style>
  :root {
    --brand-pink: #d81c6c;
    --card-white: #f7f7f7;
    --text-grey: #555555;
    --swoosh-grey: #bdbdbd;
    --backdrop: #e6e6e6;
  }
  html, body {
    margin: 0;
    padding: 0;
    width: 1200px;
    height: 900px;
    overflow: hidden;
    background: var(--backdrop);
    font-family: "Arimo", Arial, sans-serif;
  }
  .sheet {
    position: relative;
    width: 1200px;
    height: 900px;
  }
  .card {
    position: absolute;
    left: 250px;
    width: 700px;
    height: 400px;
    overflow: hidden;
    box-shadow: 0 4px 14px rgba(0,0,0,0.18);
  }
  .card-front {
    top: 35px;
    background: var(--brand-pink);
    display: flex;
    align-items: center;
    justify-content: center;
  }
  .card-front .brand-name {
    color: #f2f2f2;
    font-size: 64px;
    font-weight: 400;
    letter-spacing: 1px;
  }
  .card-back {
    top: 465px;
    background: var(--card-white);
  }
  .card-back .swoosh {
    position: absolute;
    inset: 0;
  }
  .card-back .brand-name {
    position: absolute;
    left: 50px;
    top: 160px;
    width: 320px;
    text-align: center;
    color: var(--brand-pink);
    font-size: 44px;
    font-weight: 400;
  }
  .divider {
    position: absolute;
    left: 395px;
    top: 70px;
    width: 2px;
    height: 215px;
    background: var(--brand-pink);
  }
  .contact-block {
    position: absolute;
    left: 418px;
    top: 66px;
    color: var(--text-grey);
  }
  .person-name {
    margin: 0;
    color: var(--brand-pink);
    font-size: 22px;
    font-weight: 700;
    letter-spacing: 1px;
  }
  .person-role {
    margin: 2px 0 18px;
    font-size: 15px;
    letter-spacing: 0.5px;
  }
  .address {
    margin: 0 0 16px;
    font-size: 15px;
    line-height: 21px;
    letter-spacing: 0.5px;
  }
  .contact-list {
    list-style: none;
    margin: 0;
    padding: 0;
    font-size: 15px;
    line-height: 20px;
    letter-spacing: 0.4px;
  }
  .contact-list li {
    display: flex;
    align-items: center;
    gap: 8px;
  }
  .contact-list svg {
    width: 13px;
    height: 13px;
    fill: var(--brand-pink);
    flex: none;
  }
</style>
</head>
<body>
<main class="sheet">
  <section class="card card-front" aria-label="Card front">
    <span class="brand-name">Dore Lumia</span>
  </section>

  <section class="card card-back" aria-label="Card back">
    <svg class="swoosh" viewBox="0 0 700 400" preserveAspectRatio="none" aria-hidden="true">
      <path d="M300 352 Q 540 330 700 222 L700 244 Q 540 342 300 352 Z" fill="var(--swoosh-grey)"/>
      <path d="M0 322 Q 380 372 700 250 L700 400 L0 400 Z" fill="var(--brand-pink)"/>
    </svg>

    <span class="brand-name">Dore Lumia</span>
    <div class="divider"></div>

    <div class="contact-block">
      <h1 class="person-name">MARTA REYES</h1>
      <p class="person-role">President</p>
      <p class="address">West 18th Avenue, Suite 410<br>Harbor City, NY 10200</p>
      <ul class="contact-list">
        <li>
          <svg viewBox="0 0 16 16"><path d="M3 1l3 3-2 2c1 2 3 4 5 5l2-2 3 3-2 3C6 15 1 10 1 3z"/></svg>
          00 5550 123 401
        </li>
        <li>
          <svg viewBox="0 0 16 16"><path d="M4 0h8a1 1 0 011 1v14a1 1 0 01-1 1H4a1 1 0 01-1-1V1a1 1 0 011-1zm1 2v10h6V2zm3 11a1 1 0 100 2 1 1 0 000-2z"/></svg>
          00 5550 123 402
        </li>
        <li>
          <svg viewBox="0 0 16 16"><path d="M0 3h16v10H0zM1 4l7 5 7-5v-0.5H1z" fill-rule="evenodd"/><path d="M1 4.5l7 5 7-5" fill="none" stroke="#fff" stroke-width="1"/></svg>
          yourmail@dorelumia.com
        </li>
        <li>
          <svg viewBox="0 0 16 16"><circle cx="8" cy="8" r="7.5"/><path d="M0.5 8h15M8 0.5v15M2.5 4h11M2.5 12h11" stroke="#fff" stroke-width="0.9" fill="none"/><ellipse cx="8" cy="8" rx="3.2" ry="7.5" fill="none" stroke="#fff" stroke-width="0.9"/></svg>
          www.dorelumia.com
        </li>
      </ul>
    </div>
  </section>
</main>
</body>
</html>
```